Simple, High-Class Web Design Wanted - Motivational Speakers Site

1. Full Brief/Request & Specs outlined on following video -
http://clipvarnish-demo.com/watch/tRbWlKpZgQ

2. Use colours, images as you feel suits objective (we are happy to pay up to US$30 for any good images but must have licence/permission).

3. Layout probably similar to existing site - www.quillhavenorators.com.au / http://quillhavenorators.com.au/contact.php

4. Must Be Able to Coded for MOBILE-FRIENDLINESS & WordPress friendly Ideal.

5. This is the first, small job of many we/graphic design jobs. If suits, winning designer may be offered all future work direct.

Thanks & look forward to your design. Doug.

Target Market(s)

corporates - high end

Number of Pages Required

2 page

Font styles to use
Sans Serif

Requirements
Must have
• Classy professional look
Nice to have
• all in Video in brief
Should not have
• too many images / new images I haven't approved

```html
<!DOCTYPE html>
<html lang="en">
<head>
<meta charset="utf-8">
<title>Quillhaven Orators – Conference Speakers</title>
<link href="https://fonts.googleapis.com/css2?family=Open+Sans:wght@300;400;600;700&display=swap" rel="stylesheet">
<style>
:root{
  --teal:#1b7d93;
  --teal-dark:#14637a;
  --ink:#3c4650;
  --muted:#6b7780;
  --white:#ffffff;
  --night:#101b24;
  --footer:#13273a;
  --footer-bar:#0b1822;
  --band:#3d7d92;
}
*{box-sizing:border-box;margin:0;padding:0}
html,body{width:1200px;height:2816px;overflow:hidden}
body{font-family:"Open Sans",Arial,sans-serif;color:var(--ink);background:var(--white);position:relative}
section,header,footer{position:absolute;left:0;width:1200px;overflow:hidden}
.abs{position:absolute}
.section-title{position:absolute;left:0;width:100%;text-align:center;font-size:38px;font-weight:400;color:var(--teal)}
.divider{position:absolute;width:120px;height:16px}

/* hero */
.hero{top:0;height:652px;background:linear-gradient(100deg,#2b2f33 0%,#4a4e52 35%,#6e6a63 60%,#8a7d6c 100%)}
.hero-photo{position:absolute;inset:0;background:radial-gradient(ellipse at 22% 55%,#5a5550 0%,rgba(40,40,42,0) 45%),linear-gradient(180deg,rgba(0,0,0,.1),rgba(0,0,0,.45))}
.topbar{position:absolute;top:0;left:0;width:100%;height:112px;background:rgba(255,255,255,.12)}
.brand{position:absolute;left:66px;top:28px;display:flex;align-items:center;gap:14px}
.brand-dot{width:40px;height:40px;border-radius:50%;background:var(--teal)}
.brand-name{font-size:30px;font-weight:600;color:var(--white);letter-spacing:1px}
.nav{position:absolute;right:68px;top:0;display:flex;height:112px}
.nav a{display:flex;align-items:center;padding:0 22px;color:var(--white);font-size:17px;text-decoration:none;letter-spacing:.5px}
.nav a.active{background:var(--teal)}
.hero-copy{position:absolute;right:60px;top:270px;width:820px;text-align:right}
.hero-copy h1{font-size:42px;font-weight:300;color:var(--white);line-height:54px}
.hero-copy p{font-size:24px;color:#dfe6ea;line-height:32px;margin-top:6px}
.dots{position:absolute;top:620px;left:0;width:100%;display:flex;justify-content:center;gap:14px}
.dots span{width:14px;height:14px;border-radius:50%;border:2px solid var(--white)}
.dots span.on{background:var(--white)}

/* about */
.about{top:652px;height:348px;background:var(--white)}
.about-text{position:absolute;left:88px;top:132px;width:660px;text-align:center;font-size:15px;line-height:24px;color:var(--muted)}
.btn{position:absolute;display:flex;align-items:center;justify-content:center;font-size:17px;color:var(--white);border-radius:24px;text-decoration:none}
.btn-solid{background:var(--teal-dark)}
.btn-ghost{border:2px solid var(--white)}
.about-photo{position:absolute;left:772px;top:8px;width:388px;height:340px;background:linear-gradient(180deg,#e9eef2 0%,#b9c7d6 70%,#7d96b5 100%)}

/* video */
.videos{top:1000px;height:540px;background:linear-gradient(180deg,#1c2128 0%,#2a2d31 50%,#171b20 100%)}
.video-card{position:absolute;top:132px;width:330px}
.video-thumb{height:188px;position:relative;background:linear-gradient(135deg,#6b5a4a,#3d4a5a 60%,#8a7c6a)}
.video-thumb svg{position:absolute;left:50%;top:50%;transform:translate(-50%,-50%)}
.video-card h3{margin-top:26px;text-align:center;font-size:28px;font-weight:400;color:var(--white)}
.video-card p{text-align:center;font-size:15px;line-height:21px;color:#cfd6db;padding:0 22px}

/* speakers */
.speakers{top:1540px;height:440px;background:var(--white)}
.speaker{position:absolute;top:168px;width:170px;height:166px}
.speaker-social{position:absolute;left:0;bottom:0;width:100%;height:34px;background:rgba(27,125,147,.85);display:flex;align-items:center;gap:8px;padding-left:10px}
.speaker-social i{width:18px;height:18px;border-radius:50%;background:var(--white);display:block}
.pager{position:absolute;top:356px;left:564px;display:flex;gap:8px}
.pager span{width:34px;height:34px;display:flex;align-items:center;justify-content:center;border:1px solid #c9d2d8}
.pager span.on{background:var(--teal);border-color:var(--teal)}

/* categories */
.categories{top:1980px;height:548px;background:linear-gradient(180deg,#5f93a6 0%,var(--band) 45%,#2e6b80 100%)}
.cat-intro{position:absolute;left:300px;top:106px;width:600px;text-align:center;font-size:15px;line-height:24px;color:var(--white)}
.cat-col{position:absolute;top:200px;width:320px;text-align:center;color:var(--white)}
.cat-col h3{font-size:28px;font-weight:300}
.cat-col ul{list-style:none;margin-top:18px}
.cat-col li{font-size:15px;line-height:29px;color:#e6eef1}

/* footer */
.site-footer{top:2528px;height:232px;background:var(--footer);color:var(--white)}
.foot-col{position:absolute;top:44px}
.foot-col h4{font-size:22px;font-weight:400;margin-bottom:18px}
.foot-col li{list-style:none;font-size:14px;line-height:22px;color:#cdd7de}
.contact-row{display:flex;align-items:center;gap:12px;font-size:14px;color:#cdd7de;margin-bottom:12px}
.follow{font-size:15px;margin-top:8px}
.social{display:flex;gap:12px;margin-top:10px}
.social i{width:26px;height:26px;border-radius:50%;background:var(--white);display:block}
.field{width:312px;height:40px;background:var(--white);color:#8a949b;font-size:14px;padding:10px 14px}
.submit{width:150px;height:38px;margin-top:18px;background:var(--teal);border-radius:20px;display:flex;align-items:center;justify-content:center;font-size:15px}
.footer-bar{top:2760px;height:56px;background:var(--footer-bar);color:#aab6bf;font-size:14px;display:flex;align-items:center;justify-content:center}
</style>
</head>
<body>

<header class="hero">
  <div class="hero-photo" role="img" aria-label="Keynote speaker in a suit presenting in front of a conference audience"></div>
  <div class="topbar"></div>
  <div class="brand"><span class="brand-dot"></span><span class="brand-name">Quillhaven Orators</span></div>
  <nav class="nav">
    <a class="active" href="#">HOME</a>
    <a href="#">ABOUT US</a>
    <a href="#">SPEAKERS</a>
    <a href="#">ENTERTAINMENT</a>
    <a href="#">CONTACT US</a>
  </nav>
  <div class="hero-copy">
    <h1>Are you looking for a Guest or Keynote Speaker - Inspiring, Entertaining, for a conference</h1>
    <p>Lorem Ipsum is simply dummy text of the printing and<br>typesetting industry</p>
  </div>
  <div class="dots"><span></span><span class="on"></span><span></span></div>
</header>

<section class="about">
  <h2 class="section-title" style="width:836px;top:38px">Know More About Us</h2>
  <svg class="divider" style="left:358px;top:96px" viewBox="0 0 120 16"><line x1="0" y1="8" x2="50" y2="8" stroke="#1b7d93" stroke-width="2"/><circle cx="60" cy="8" r="5" fill="#1b7d93"/><line x1="70" y1="8" x2="120" y2="8" stroke="#1b7d93" stroke-width="2"/></svg>
  <p class="about-text">Quillhaven Orators is a free industry service designed to help people looking for speakers save precious time and frustration in finding the most suitable keynote speaker for their needs. Suggestions are given by our conference speaker Doug Ferrell, who has presented around Australia for a number of years.</p>
  <a class="btn btn-solid" href="#" style="left:342px;top:248px;width:152px;height:46px">Read More</a>
  <div class="about-photo" role="img" aria-label="Portrait of the founder in a blue checked shirt"></div>
</section>

<section class="videos" role="region" aria-label="Latest video">
  <h2 class="section-title" style="top:36px;color:var(--white)">See Our Latest Video</h2>
  <svg class="divider" style="left:540px;top:92px" viewBox="0 0 120 16"><line x1="0" y1="8" x2="50" y2="8" stroke="#fff" stroke-width="2"/><circle cx="60" cy="8" r="5" fill="#1b7d93"/><line x1="70" y1="8" x2="120" y2="8" stroke="#fff" stroke-width="2"/></svg>

  <div class="video-card" style="left:72px">
    <div class="video-thumb" role="img" aria-label="Speaker on stage before a seated audience"><svg width="56" height="56" viewBox="0 0 56 56"><circle cx="28" cy="28" r="26" fill="#1b7d93" stroke="#fff" stroke-width="3"/><path d="M22 17 L40 28 L22 39 Z" fill="#fff"/></svg></div>
    <h3>Lorem Ipsum</h3>
    <p>Lorem Ipsum is simply dummy text of the printing and typesetting industry</p>
  </div>
  <div class="video-card" style="left:435px">
    <div class="video-thumb" role="img" aria-label="Presenter speaking at a lectern"><svg width="56" height="56" viewBox="0 0 56 56"><circle cx="28" cy="28" r="26" fill="#1b7d93" stroke="#fff" stroke-width="3"/><path d="M22 17 L40 28 L22 39 Z" fill="#fff"/></svg></div>
    <h3>Lorem Ipsum</h3>
    <p>Lorem Ipsum is simply dummy text of the printing and typesetting industry</p>
  </div>
  <div class="video-card" style="left:798px">
    <div class="video-thumb" role="img" aria-label="Conference hall with audience facing the stage"><svg width="56" height="56" viewBox="0 0 56 56"><circle cx="28" cy="28" r="26" fill="#1b7d93" stroke="#fff" stroke-width="3"/><path d="M22 17 L40 28 L22 39 Z" fill="#fff"/></svg></div>
    <h3>Lorem Ipsum</h3>
    <p>Lorem Ipsum is simply dummy text of the printing and typesetting industry</p>
  </div>
  <a class="btn btn-ghost" href="#" style="left:540px;top:464px;width:120px;height:42px">View All</a>
</section>

<section class="speakers">
  <h2 class="section-title" style="top:44px">Find A Speaker For Your Next Event</h2>
  <svg class="divider" style="left:540px;top:100px" viewBox="0 0 120 16"><line x1="0" y1="8" x2="50" y2="8" stroke="#1b7d93" stroke-width="2"/><circle cx="60" cy="8" r="5" fill="#1b7d93"/><line x1="70" y1="8" x2="120" y2="8" stroke="#1b7d93" stroke-width="2"/></svg>
  <div class="speaker" style="left:72px;background:linear-gradient(180deg,#c9b79e,#8d7a66)" role="img" aria-label="Speaker portrait"><div class="speaker-social"><i></i><i></i><i></i><i></i></div></div>
  <div class="speaker" style="left:249px;background:linear-gradient(180deg,#b8b2ab,#5c5c60)" role="img" aria-label="Speaker portrait"></div>
  <div class="speaker" style="left:426px;background:linear-gradient(180deg,#d7cdc3,#7b3a3a)" role="img" aria-label="Speaker portrait"></div>
  <div class="speaker" style="left:603px;background:linear-gradient(180deg,#c3c5c8,#404754)" role="img" aria-label="Speaker portrait"></div>
  <div class="speaker" style="left:780px;background:linear-gradient(180deg,#bcbcbc,#2f3640)" role="img" aria-label="Speaker portrait"></div>
  <div class="speaker" style="left:957px;background:linear-gradient(180deg,#a9a29c,#3a3330)" role="img" aria-label="Speaker portrait"></div>
  <div class="pager">
    <span><svg width="12" height="14" viewBox="0 0 12 14"><path d="M9 1 L3 7 L9 13" fill="none" stroke="#6b7780" stroke-width="2"/></svg></span>
    <span class="on"><svg width="12" height="14" viewBox="0 0 12 14"><path d="M3 1 L9 7 L3 13" fill="none" stroke="#fff" stroke-width="2"/></svg></span>
  </div>
</section>

<section class="categories" role="region" aria-label="Speaker categories">
  <h2 class="section-title" style="top:36px;color:var(--white);font-weight:300">Popular Speakers In Categories</h2>
  <p class="cat-intro">If you would like a hand finding some good speaker options, simply send us the details of your event and the type of presenter you are ideally after.</p>
  <div class="cat-col" style="left:80px">
    <h3>Type/Style</h3>
    <ul><li>Motivational</li><li>Entertaining</li><li>Seminar/Workshop</li><li>Master of Ceremonies (MC's)</li><li>Business Speakers</li><li>Sports Speakers</li><li>Kids Speakers</li></ul>
  </div>
  <div class="cat-col" style="left:440px">
    <h3>Location</h3>
    <ul><li>Sydney</li><li>Melbourne</li><li>Brisbane</li><li>Perth</li><li>Adelaide</li><li>Canberra etc.</li></ul>
  </div>
  <div class="cat-col" style="left:800px">
    <h3>Topic/Area</h3>
    <ul><li>Team Building</li><li>Leadership</li><li>Inspiration</li><li>Health &amp; Life Balance</li></ul>
  </div>
</section>

<footer class="site-footer">
  <div class="foot-col" style="left:72px">
    <h4>Usefull Links</h4>
    <ul><li>HOME</li><li>ABOUT US</li><li>SPEAKERS</li><li>ENTERTAINMENT</li><li>CONTACT US</li></ul>
  </div>
  <div class="foot-col" style="left:448px">
    <h4>Keep In Touch</h4>
    <div class="contact-row"><svg width="18" height="14" viewBox="0 0 18 14"><rect x="1" y="1" width="16" height="12" fill="none" stroke="#fff" stroke-width="1.5"/><path d="M1 1 L9 8 L17 1" fill="none" stroke="#fff" stroke-width="1.5"/></svg>support@quillhavenorators.com.au</div>
    <div class="contact-row"><svg width="18" height="18" viewBox="0 0 18 18"><path d="M4 1 L7 5 L5 7 C6 10 8 12 11 13 L13 11 L17 14 L15 17 C8 17 1 10 1 3 Z" fill="#fff"/></svg>1 300 47 62 19</div>
    <div class="follow">Follow Us</div>
    <div class="social"><i></i><i></i><i></i></div>
  </div>
  <div class="foot-col" style="left:808px">
    <h4>Subscribe Here to get Update</h4>
    <div class="field">Email ID</div>
    <div class="submit">Submit</div>
  </div>
</footer>
<div class="footer-bar abs" style="left:0;width:1200px">© 2015. All Rights Reserved</div>

</body>
</html>
```